Lantern

My company name is lantern. The logo is attached. I am the business owner.
Name Gordon Pileck
Phone number- 2018347265
email- Gordon_pileck@mailbrook.net
Website is not live yet but it will be workwithlantern.com
the current beta link is- https://site.qvbtstage.com/lantern-v3/
on the back write “ find creative pros”
Use that beta link as reference for typography and colors on card.

```html
<!DOCTYPE html>
<html lang="en">
<head>
<meta charset="utf-8">
<title>Lantern – Business Card</title>
<link href="https://fonts.googleapis.com/css2?family=Montserrat:wght@500;800&family=Arimo:wght@400&display=swap" rel="stylesheet">
<style>
  :root {
    --bg: #2a2a2a;
    --card-black: #050505;
    --card-dark: #111111;
    --amber: #f29a1a;
    --amber-deep: #c9780f;
    --white: #f2f2f2;
    --muted: #d8d8d8;
    --rule-grey: #8a8a8a;
  }
  * { margin: 0; padding: 0; box-sizing: border-box; }
  html, body {
    width: 1200px; height: 900px; overflow: hidden;
    background: var(--bg);
  }
  .canvas { position: relative; width: 1200px; height: 900px; }

  .card {
    position: absolute; left: 240px;
    width: 720px; height: 410px;
    border-radius: 26px; overflow: hidden;
    box-shadow: 0 14px 30px rgba(0,0,0,.45);
  }

  /* Front */
  .card-front {
    top: 30px;
    background: linear-gradient(100deg, var(--card-black) 0%, var(--card-dark) 38%, var(--amber-deep) 72%, var(--amber) 100%);
  }
  .card-front .wordmark {
    position: absolute; left: 300px; top: 130px;
    font-family: "Montserrat", sans-serif; font-weight: 800;
    font-size: 74px; letter-spacing: 1px; color: var(--white);
  }
  .card-front .tagline {
    position: absolute; left: 360px; top: 250px;
    font-family: "Arimo", sans-serif; font-size: 21px;
    letter-spacing: 1px; color: var(--white);
  }

  /* Back */
  .card-back {
    top: 460px;
    background: linear-gradient(160deg, var(--card-dark) 0%, var(--card-black) 60%);
  }
  .card-back .wordmark {
    position: absolute; left: 50px; top: 40px;
    font-family: "Montserrat", sans-serif; font-weight: 800;
    font-size: 66px; letter-spacing: 1px; color: var(--white);
  }
  .contact-person { position: absolute; left: 50px; top: 215px; width: 380px; }
  .person-name {
    font-family: "Montserrat", sans-serif; font-weight: 800;
    font-size: 31px; color: var(--amber); letter-spacing: .5px;
    padding-bottom: 8px; border-bottom: 1px solid var(--rule-grey);
    width: 380px; white-space: nowrap;
  }
  .contact-list { list-style: none; margin-top: 12px; }
  .contact-list li {
    display: flex; align-items: center; gap: 14px;
    font-family: "Arimo", sans-serif; font-size: 21px;
    color: var(--white); line-height: 34px; white-space: nowrap;
  }
  .contact-list svg { width: 20px; height: 20px; flex: none; }

  .contact-web {
    position: absolute; left: 450px; top: 200px; width: 250px;
  }
  .web-rule { height: 1px; background: var(--amber); width: 250px; margin-bottom: 14px; }
  .web-list { list-style: none; }
  .web-list li {
    display: flex; align-items: center; gap: 10px;
    font-family: "Arimo", sans-serif; font-size: 15px;
    color: var(--white); line-height: 28px; white-space: nowrap;
  }
  .web-list svg { width: 18px; height: 18px; flex: none; }
</style>
</head>
<body>
<main class="canvas">

  <section class="card card-front" aria-label="Card front">
    <div class="wordmark">LANTERN</div>
    <div class="tagline">FIND CREATIVE PROS</div>
  </section>

  <section class="card card-back" aria-label="Card back">
    <div class="wordmark">LANTERN</div>

    <div class="contact-person">
      <div class="person-name">GORDON PILECK</div>
      <ul class="contact-list">
        <li>
          <svg viewBox="0 0 24 24" aria-hidden="true"><path fill="#f29a1a" d="M6.6 10.8a15.1 15.1 0 0 0 6.6 6.6l2.2-2.2a1 1 0 0 1 1-.25 11.4 11.4 0 0 0 3.6.57 1 1 0 0 1 1 1V20a1 1 0 0 1-1 1A17 17 0 0 1 3 4a1 1 0 0 1 1-1h3.5a1 1 0 0 1 1 1c0 1.25.2 2.45.57 3.57a1 1 0 0 1-.25 1z"/></svg>
          2018347265
        </li>
        <li>
          <svg viewBox="0 0 24 24" aria-hidden="true"><rect x="2" y="5" width="20" height="14" fill="#f29a1a"/><path d="M2 5l10 8 10-8" fill="none" stroke="#050505" stroke-width="1.6"/></svg>
          Gordon_pileck@mailbrook.net
        </li>
      </ul>
    </div>

    <div class="contact-web">
      <div class="web-rule"></div>
      <ul class="web-list">
        <li>
          <svg viewBox="0 0 24 24" aria-hidden="true"><circle cx="12" cy="12" r="10" fill="#f29a1a"/><path d="M2 12h20M12 2c3 3 3 17 0 20M12 2c-3 3-3 17 0 20" fill="none" stroke="#050505" stroke-width="1.5"/></svg>
          workwithlantern.com
        </li>
        <li>
          <svg viewBox="0 0 24 24" aria-hidden="true"><circle cx="12" cy="12" r="10" fill="#f29a1a"/><path d="M2 12h20M12 2c3 3 3 17 0 20M12 2c-3 3-3 17 0 20" fill="none" stroke="#050505" stroke-width="1.5"/></svg>
          site.qvbtstage.com/lantern-v3/
        </li>
      </ul>
    </div>
  </section>

</main>
</body>
</html>
```